"KTR Community Supports" Business Card Design

We are a not for profit disability service that has recently changed its logo and trading name and is in the process of "rebranding".We provide employment, training and accommodation to people with disabilities. We find our new logo fresh and inspiring and would like our new business cards to reflect the same feeling. Our marketing line is "Growth, Opportunity, Empowerment".

Target Market(s)

People with disabilities and their families, carers, support network

Industry/Entity Type

Business

Contact Information for Business Card

Requirements
Must have
• Our logo; space for the above listed information requirements

```html
<!DOCTYPE html>
<html lang="en">
<head>
<meta charset="utf-8">
<title>KTR Community Supports – Business Card</title>
<link rel="stylesheet" href="https://fonts.googleapis.com/css2?family=Michroma&display=swap">
<style>
  :root {
    --backdrop: #e6e8ec;
    --card: #f4f5f4;
    --navy: #0b3a7e;
    --blue: #0a6fbf;
    --green: #5e9a2c;
    --ink: #2b2f36;
    --white: #ffffff;
    --ghost: #e3e7e4;
  }
  * { box-sizing: border-box; margin: 0; padding: 0; }
  html, body { width: 1200px; height: 840px; overflow: hidden; background: var(--backdrop); }
  body { font-family: "Michroma", sans-serif; }
  .card {
    position: absolute; left: 100px; top: 134px;
    width: 1000px; height: 572px;
    background: var(--card);
    box-shadow: 0 6px 22px rgba(0,0,0,0.18);
    overflow: hidden;
  }
  .card-art { position: absolute; inset: 0; width: 100%; height: 100%; }
  .holder-name {
    position: absolute; right: 38px; top: 38px; text-align: right; color: var(--white);
  }
  .holder-name .person { font-size: 30px; letter-spacing: 1px; line-height: 1.2; }
  .holder-name .role { font-size: 20px; line-height: 1.3; }
  .brand {
    position: absolute; right: 44px; top: 268px;
    display: flex; align-items: center; gap: 14px;
  }
  .brand-dot { width: 46px; height: 46px; border-radius: 50%; background: var(--green); }
  .brand-name { font-size: 54px; color: var(--navy); letter-spacing: 2px; line-height: 1; }
  .address {
    position: absolute; right: 44px; top: 392px; text-align: right;
    font-size: 19px; line-height: 1.45; color: var(--ink);
  }
  .contacts {
    position: absolute; left: 40px; bottom: 36px; list-style: none;
    font-size: 15px; color: var(--ink);
  }
  .contacts li { display: flex; align-items: center; gap: 12px; height: 31px; }
  .contacts svg { width: 18px; height: 18px; fill: var(--ink); flex: none; }
</style>
</head>
<body>
  <main class="card">
    <svg class="card-art" viewBox="0 0 1000 572" preserveAspectRatio="none" aria-hidden="true">
      <defs>
        <linearGradient id="bandFill" x1="0" y1="0" x2="1" y2="0.3">
          <stop offset="0" stop-color="#0a3577"/>
          <stop offset="0.55" stop-color="#0a74c4"/>
          <stop offset="1" stop-color="#0b3a84"/>
        </linearGradient>
      </defs>
      <path class="top-band" fill="url(#bandFill)"
            d="M0 0 H1000 V250 C860 215 710 172 560 176 C330 184 120 220 0 300 Z"/>
      <path class="green-sweep" fill="var(--green)"
            d="M0 318 C120 238 320 188 560 178 C330 204 120 268 18 430 L0 450 Z"/>
      <path class="white-swoosh" fill="var(--white)"
            d="M620 236 C770 222 900 190 1000 150 L1000 166 C900 206 770 234 620 236 Z"/>
      <circle class="ghost-mark" cx="460" cy="400" r="92" fill="var(--ghost)" opacity="0.7"/>
    </svg>

    <header class="holder-name">
      <p class="person">DANIEL MERCER</p>
      <p class="role">Managing Director</p>
    </header>

    <div class="brand">
      <span class="brand-dot"></span>
      <span class="brand-name">KTR</span>
    </div>

    <address class="address" style="font-style:normal">
      027.4th floor,Arcade<br>Harbour Lane Road QLD
    </address>

    <ul class="contacts">
      <li><svg viewBox="0 0 24 24"><path d="M6.6 10.8a15 15 0 0 0 6.6 6.6l2.2-2.2a1 1 0 0 1 1-.25 11.4 11.4 0 0 0 3.6.57 1 1 0 0 1 1 1V20a1 1 0 0 1-1 1A17 17 0 0 1 3 4a1 1 0 0 1 1-1h3.5a1 1 0 0 1 1 1c0 1.25.2 2.45.57 3.57a1 1 0 0 1-.25 1z"/></svg>012 555 0148</li>
      <li><svg viewBox="0 0 24 24"><path d="M7 1h10a2 2 0 0 1 2 2v18a2 2 0 0 1-2 2H7a2 2 0 0 1-2-2V3a2 2 0 0 1 2-2zm0 3v14h10V4zm5 15.5a1 1 0 1 0 0 2 1 1 0 0 0 0-2z"/></svg>012 555 0149</li>
      <li><svg viewBox="0 0 24 24"><path d="M6 2h9l3 3v5h2a2 2 0 0 1 2 2v10H2V12a2 2 0 0 1 2-2h2zm2 2v6h8V6h-2V4zm-2 11v2h3v-2zm5 0v2h3v-2zm5 0v2h3v-2z"/></svg>012 555 0150</li>
      <li><svg viewBox="0 0 24 24"><path d="M2 5h20v14H2zm2 2v.5l8 5 8-5V7zm0 2.8V17h16V9.8l-8 5z"/></svg>hello@ktrcs.org</li>
      <li><svg viewBox="0 0 24 24"><path d="M12 2a10 10 0 1 0 0 20 10 10 0 0 0 0-20zm6.9 9h-3a15 15 0 0 0-1.3-5.6A8 8 0 0 1 18.9 11zM12 4c.9 1.2 1.8 3.6 1.9 7h-3.8C10.2 7.6 11.1 5.2 12 4zM9.4 5.4A15 15 0 0 0 8.1 11h-3a8 8 0 0 1 4.3-5.6zM5.1 13h3a15 15 0 0 0 1.3 5.6A8 8 0 0 1 5.1 13zM12 20c-.9-1.2-1.8-3.6-1.9-7h3.8c-.1 3.4-1 5.8-1.9 7zm2.6-1.4a15 15 0 0 0 1.3-5.6h3a8 8 0 0 1-4.3 5.6z"/></svg>www.ktrsupports.org</li>
    </ul>
  </main>
</body>
</html>
```